They say laughter is the best medicine

This poster is for a nursing pharmacology class room with 70+students. Size is 24" x36". It needs to be a clean design. Would like vintage advertisement banners and script fonts. Would like a black background with an accent color. Please view pictures on word doc for examples.

```html
<!DOCTYPE html>
<html lang="en">
<head>
<meta charset="utf-8">
<title>Laughter Is the Best Medicine – Nursing Pharmacology Concepts</title>
<link rel="stylesheet" href="https://fonts.googleapis.com/css2?family=Berkshire+Swash&family=Marcellus+SC&family=Yesteryear&display=swap">
<style>
  :root {
    --page: #ecebea;
    --board: #1f1f1f;
    --board-light: #2c2c2c;
    --coral: #e0674a;
    --mint: #c3e4d4;
    --chalk: #f1f1ec;
  }
  * { margin: 0; padding: 0; box-sizing: border-box; }
  html, body { width: 1200px; height: 1138px; overflow: hidden; background: var(--page); }

  .poster {
    position: absolute; left: 203px; top: 19px; width: 794px; height: 1100px;
    background: radial-gradient(ellipse at 50% 40%, var(--board-light), var(--board) 75%);
    color: var(--chalk);
  }
  .frame {
    position: absolute; left: 18px; right: 18px; top: 48px; bottom: 55px;
    border: 2px solid var(--coral);
  }
  .ornament {
    position: absolute; background: var(--coral); opacity: .85; border-radius: 40px;
  }
  .ornament--top { left: 310px; top: 38px; width: 174px; height: 20px; }
  .ornament--scroll-left { left: 54px; top: 420px; width: 136px; height: 18px; transform: rotate(18deg); }
  .ornament--scroll-right { right: 54px; top: 420px; width: 136px; height: 18px; transform: rotate(-18deg); }

  .headline { position: absolute; left: 0; right: 0; text-align: center; }
  .headline--intro {
    top: 96px; font-family: "Berkshire Swash", cursive; font-size: 74px; color: var(--mint);
  }
  .headline--quote {
    top: 196px; font-family: "Berkshire Swash", cursive; font-size: 68px; line-height: 66px; color: var(--coral);
  }
  .headline--answer {
    top: 342px; font-family: "Marcellus SC", serif; font-size: 54px; color: var(--mint); letter-spacing: 1px;
  }

  .drug-list {
    position: absolute; top: 468px; width: 240px; list-style: none; text-align: center;
    font-family: "Marcellus SC", serif; font-size: 24px; line-height: 35px;
  }
  .drug-list--left { left: 44px; }
  .drug-list--right { left: 522px; }
  .coral { color: var(--coral); }
  .mint { color: var(--mint); }
  .chalk { color: var(--chalk); }

  .nurse-halo {
    position: absolute; left: 262px; top: 470px; width: 290px; height: 290px; border-radius: 50%;
    background: #3a3a3a;
  }
  .nurse-illustration {
    position: absolute; left: 250px; top: 446px; width: 320px; height: 394px;
    background: linear-gradient(180deg, #e8e8e6 0%, #b9b9b9 45%, #222 70%, #f0f0f0 100%);
    clip-path: polygon(25% 0, 75% 0, 88% 35%, 100% 100%, 0 100%, 12% 35%);
  }

  .tagline {
    position: absolute; left: 0; right: 0; top: 882px; text-align: center;
    font-family: "Marcellus SC", serif; font-size: 21px; color: var(--mint);
  }
  .course-title {
    position: absolute; left: 0; right: 0; top: 912px; text-align: center;
    font-family: "Yesteryear", cursive; font-size: 48px; color: var(--chalk);
  }
  .instructor {
    position: absolute; left: 0; right: 0; top: 976px; text-align: center;
    font-family: "Marcellus SC", serif; font-size: 24px; color: var(--coral); letter-spacing: .5px;
  }
  .role {
    position: absolute; left: 50%; top: 1031px; transform: translateX(-50%);
    padding: 0 16px; background: var(--board); white-space: nowrap;
    font-family: "Marcellus SC", serif; font-size: 20px; color: var(--chalk);
  }
</style>
</head>
<body>
  <main class="poster">
    <div class="frame"></div>
    <div class="ornament ornament--top" role="img" aria-label="Red decorative flourish"></div>

    <h1 class="headline headline--intro">They say</h1>
    <p class="headline headline--quote">“Laughter<br>is the best medicine”</p>
    <div class="ornament ornament--scroll-left" role="img" aria-label="Red curled banner scroll"></div>
    <div class="ornament ornament--scroll-right" role="img" aria-label="Red curled banner scroll"></div>
    <p class="headline headline--answer">Well, we think</p>

    <ul class="drug-list drug-list--left">
      <li class="coral">Acetaminophen</li>
      <li class="mint">Lorazepam</li>
      <li class="coral">MS04</li>
      <li class="chalk">Furosemide</li>
      <li class="mint">Nitroglycerin</li>
      <li class="coral">Haloperidol</li>
    </ul>

    <div class="nurse-halo"></div>
    <div class="nurse-illustration" role="img" aria-label="Vintage comic-style illustration of a smiling nurse in a white cap and uniform"></div>

    <ul class="drug-list drug-list--right">
      <li class="coral">Loperamide</li>
      <li class="mint">Albuterol</li>
      <li class="coral">Vancomycin</li>
      <li class="chalk">Insulin</li>
      <li class="coral">&amp;</li>
      <li class="coral">Oxygen</li>
    </ul>

    <p class="tagline">Just might be what you want more in certain situations.</p>
    <h2 class="course-title">Nursing Pharmacology Concepts</h2>
    <p class="instructor">Jolene Harwick, PhD, MSN, RN, CCRN, CPN, CNE</p>
    <p class="role">Clinical Professor</p>
  </main>
</body>
</html>
```